Plumbing business cards for plumbing company

Need business cards made for my plumbing company

Darren Holcott
253-555-0187
Darren@TrueFlowPipeworksExample.com
www .TrueFlowpipeworksexample.com

https://brightlanehosting.example/wp-content/uploads/2024/03/TrueFlow-Pipes-Rev-04-01.jpg

https://brightlanehosting.example/wp-content/uploads/2024/03/TrueFlow-Pipes-Rev-02-01.jpg

Contact Information for Business Card

Darren Holcott 253-555-0187 Darren@TrueFlowPipeworksExample.com www .TrueFlowpipeworksexample.com

Colors
0054AA
0677BA
7BADD7
CADEEF
E8F1F8

```html
<!DOCTYPE html>
<html lang="en">
<head>
<meta charset="utf-8">
<title>TrueFlow Pipeworks – Business Cards</title>
<link rel="stylesheet" href="https://fonts.googleapis.com/css2?family=Montserrat:wght@400;600;700;800&display=swap">
<style>
  :root{
    --brand-blue:#0a438f;
    --brand-grey:#666666;
    --ink:#1c1c1c;
    --paper:#ffffff;
    --backdrop:#1a1a1a;
  }
  *{margin:0;padding:0;box-sizing:border-box}
  html,body{width:1200px;height:1059px;overflow:hidden;background:var(--backdrop)}
  body{position:relative;font-family:"Montserrat",sans-serif}
  .card{position:absolute;left:254px;width:713px;height:408px;border-radius:26px;background:var(--paper);overflow:hidden}
  .card--front{top:79px}
  .card--back{top:546px}
  .front__brand{position:absolute;left:0;right:0;top:72px;line-height:48px;text-align:center;font-weight:800;font-size:40px;color:var(--brand-blue);letter-spacing:.5px}
  .front__name{position:absolute;left:29px;top:220px;line-height:36px;font-weight:700;font-size:29px;color:var(--brand-blue)}
  .front__rule{position:absolute;left:29px;width:655px;top:270px;height:2px;background:var(--ink)}
  .contacts{position:absolute;left:29px;top:283px;list-style:none}
  .contacts li{display:flex;align-items:center;height:32.5px;font-size:20px;line-height:1;color:var(--ink);letter-spacing:.2px}
  .contacts svg{flex:none;width:18px;height:18px;margin-right:17px;fill:var(--brand-blue)}
  .front__band{position:absolute;left:0;bottom:0;width:713px;height:17px}
  .back__split{position:absolute;inset:0;width:100%;height:100%}
  .back__brand{position:absolute;left:0;right:0;top:292px;line-height:54px;text-align:center;font-weight:800;font-size:44px;color:var(--paper)}
</style>
</head>
<body>
  <section class="card card--front">
    <div class="front__brand">TrueFlow Pipeworks</div>
    <h1 class="front__name">Darren Holcott</h1>
    <div class="front__rule"></div>
    <ul class="contacts">
      <li><svg viewBox="0 0 24 24"><path d="M6.6 10.8a15.1 15.1 0 0 0 6.6 6.6l2.2-2.2c.3-.3.7-.4 1-.2 1.1.4 2.3.6 3.6.6.6 0 1 .4 1 1V20c0 .6-.4 1-1 1A17 17 0 0 1 3 4c0-.6.4-1 1-1h3.5c.6 0 1 .4 1 1 0 1.3.2 2.5.6 3.6.1.3 0 .7-.2 1z"/></svg>253-555-0187</li>
      <li><svg viewBox="0 0 24 24"><path d="M2 5h20v14H2z M2 5l10 8 10-8" stroke="#fff" stroke-width="1.5"/></svg>Darren@TrueFlowPipeworksExample.com</li>
      <li><svg viewBox="0 0 24 24"><path d="M12 2a10 10 0 1 0 0 20 10 10 0 0 0 0-20zm0 2c1 1.2 1.8 3 2.1 5H9.9C10.2 7 11 5.2 12 4zM4.3 13.5a8 8 0 0 1 0-3h3.5a16 16 0 0 0 0 3zm.8 2h3c.3 1.6.8 3 1.5 4.1a8 8 0 0 1-4.5-4.1zm3-7h-3a8 8 0 0 1 4.5-4.1C8.9 5.5 8.4 6.9 8.1 8.5zM12 20c-1-1.2-1.8-3-2.1-4.5h4.2C13.8 17 13 18.8 12 20zm2.3-6.5H9.7a14 14 0 0 1 0-3h4.6a14 14 0 0 1 0 3zm.1 6.1c.7-1.1 1.2-2.5 1.5-4.1h3a8 8 0 0 1-4.5 4.1zm1.8-6.1a16 16 0 0 0 0-3h3.5a8 8 0 0 1 0 3zm-.3-5c-.3-1.6-.8-3-1.5-4.1a8 8 0 0 1 4.5 4.1z"/></svg>www .TrueFlowpipeworksexample.com</li>
    </ul>
    <svg class="front__band" viewBox="0 0 713 17" preserveAspectRatio="none">
      <rect width="713" height="17" fill="var(--brand-grey)"/>
      <polygon points="0,0 347,0 363,17 0,17" fill="var(--brand-blue)"/>
      <polygon points="347,0 357,0 373,17 363,17" fill="var(--paper)"/>
    </svg>
  </section>

  <section class="card card--back">
    <svg class="back__split" viewBox="0 0 713 408" preserveAspectRatio="none">
      <polygon points="0,254 713,13 713,408 0,408" fill="var(--brand-blue)"/>
    </svg>
    <div class="back__brand">TrueFlow Pipeworks</div>
  </section>
</body>
</html>
```